Creative design for KWP Businesscard!

We would like a creative business card for our company The Copper Mill. We situated in Barcelona and setup software development teams for companies in Belgium, Holland.

Orange is related to Holland.
KWP means cool in Dutch

* An Overview / Background of the Business & Services
o Setup and manage developer teams in Barcelona for for companies
in Holland, Belgium.
* The Target Market / Audience you are trying to reach
o Companies in Holland searching for developers
* Design Specifics; any preferences or ideas for Style, Colour,
Imagery, etc
o Orange, professional, fancy
o The Copper Mill (KWP) means cool , good, nice

Target Market(s)

Companies in Holland searching for developers

Industry/Entity Type

Business

Contact Information for Business Card

Company name: The Copper Mill

Name: Maarten Oostveld

Title: Managing director (not necessary)

Email: maarten@thecoppermill.es

web: www.thecoppermill.es

Phone: (+34) 932 478 013

Mobile: (+34) 662 307 594

Font styles to use
Other font styles liked:
• Bookman Old Style or Rockwell

Requirements
Must have
• Setup and manage developer teams in Barcelona for for companies
• in Holland, Belgium.

```html
<!DOCTYPE html>
<html lang="en">
<head>
<meta charset="utf-8">
<title>KWP — The Copper Mill business card</title>
<link rel="stylesheet" href="https://fonts.googleapis.com/css2?family=Arvo:wght@400;700&display=swap">
<style>
  :root {
    --page-bg: #d9d6d2;
    --card-black: #050505;
    --brand-orange: #ec6e24;
    --text-white: #ffffff;
    --ghost-grey: #2e2e2e;
    --card-w: 530px;
    --card-h: 304px;
  }
  * { box-sizing: border-box; margin: 0; padding: 0; }
  html, body {
    width: 1200px; height: 813px; overflow: hidden;
    background: var(--page-bg);
    font-family: "Arvo", "Rockwell", serif;
  }
  .sheet {
    position: relative; width: 1200px; height: 813px;
    display: flex; align-items: center; justify-content: center; gap: 50px;
  }
  .card {
    position: relative; width: var(--card-w); height: var(--card-h);
    background: var(--card-black); overflow: hidden;
    box-shadow: 0 10px 26px rgba(0,0,0,.28);
  }

  /* front */
  .brand {
    position: absolute; left: 236px; top: 36px;
    display: flex; align-items: center; gap: 14px;
  }
  .brand-name {
    color: var(--text-white); font-weight: 700; font-size: 60px; line-height: 1;
    letter-spacing: 2px;
  }
  .brand-square {
    width: 18px; height: 18px; background: var(--brand-orange);
    align-self: flex-end; margin-bottom: 8px;
  }
  .phones {
    position: absolute; left: 26px; top: 112px;
    color: var(--brand-orange); font-size: 13px; line-height: 22px;
  }
  .phones li { list-style: none; display: flex; align-items: center; gap: 8px; }
  .icon { width: 15px; height: 15px; flex: none; }
  .divider {
    position: absolute; left: 26px; right: 26px; top: 168px;
    height: 1px; background: var(--brand-orange);
  }
  .person {
    position: absolute; right: 26px; top: 136px;
    color: var(--brand-orange); font-size: 22px; line-height: 1;
  }
  .email {
    position: absolute; right: 26px; top: 180px;
    display: flex; align-items: center; gap: 8px;
    color: var(--text-white); font-size: 14px; line-height: 1;
  }
  .web-band {
    position: absolute; left: 0; right: 0; top: 232px; height: 46px;
    background: var(--brand-orange);
    display: flex; align-items: center;
  }
  .web-band .rule {
    width: 200px; height: 1px; background: var(--text-white);
  }
  .website {
    margin-left: auto; margin-right: 26px;
    display: flex; align-items: center; gap: 10px;
    color: var(--text-white); font-weight: 700; font-size: 19px; line-height: 1;
  }

  /* back */
  .back-mark {
    position: absolute; left: 0; right: 0; top: 86px;
    text-align: center;
  }
  .back-mark .brand-name {
    color: var(--ghost-grey); font-size: 116px; letter-spacing: 6px;
  }
  .tagline {
    position: absolute; left: 40px; right: 40px; bottom: 34px;
    text-align: center; color: var(--brand-orange);
    font-size: 13px; line-height: 20px;
  }
</style>
</head>
<body>
<main class="sheet">

  <section class="card card-front" aria-label="Business card front">
    <div class="brand">
      <span class="brand-name">KWP</span>
      <span class="brand-square" aria-hidden="true"></span>
    </div>

    <ul class="phones">
      <li>
        <svg class="icon" viewBox="0 0 16 16" aria-hidden="true"><circle cx="8" cy="8" r="7" fill="none" stroke="#fff" stroke-width="1.2"/><path d="M6 4.5c-1 1-1 3.5 1 5.5s4 2.2 4.8 1.2l-1.3-1.3-1 .6c-.8-.4-1.7-1.3-2.1-2.1l.6-1z" fill="#fff"/></svg>
        (+34) 932 478 013
      </li>
      <li>
        <svg class="icon" viewBox="0 0 16 16" aria-hidden="true"><circle cx="8" cy="8" r="7" fill="none" stroke="#fff" stroke-width="1.2"/><rect x="5.8" y="4" width="4.4" height="8" rx=".8" fill="none" stroke="#fff" stroke-width="1.1"/></svg>
        (+34) 662 307 594
      </li>
    </ul>

    <p class="person">Maarten Oostveld</p>
    <div class="divider"></div>
    <p class="email">
      <svg class="icon" viewBox="0 0 16 12" aria-hidden="true" style="height:12px"><rect x=".6" y=".6" width="14.8" height="10.8" fill="none" stroke="#ec6e24" stroke-width="1.2"/><path d="M.6 .6 8 7l7.4-6.4M.6 11.4l5.4-5.4M15.4 11.4 10 6" fill="none" stroke="#ec6e24" stroke-width="1.2"/></svg>
      maarten@thecoppermill.es
    </p>

    <div class="web-band">
      <span class="rule"></span>
      <p class="website">
        <svg class="icon" viewBox="0 0 16 16" aria-hidden="true" style="width:18px;height:18px"><circle cx="8" cy="8" r="7" fill="none" stroke="#fff" stroke-width="1.3"/><ellipse cx="8" cy="8" rx="3" ry="7" fill="none" stroke="#fff" stroke-width="1.1"/><path d="M1 8h14" stroke="#fff" stroke-width="1.1"/></svg>
        www.thecoppermill.es
      </p>
    </div>
  </section>

  <section class="card card-back" aria-label="Business card back">
    <div class="back-mark">
      <span class="brand-name">KWP</span>
    </div>
    <p class="tagline">Setup and manage developer teams in Barcelona<br>for companies in Holland and Belgium.</p>
  </section>

</main>
</body>
</html>
```